Book Cover - Goals

Create book cover for book
Title: Summit Drive
Subtitle: Push Past Your Limits, Find Strength Within Yourself

See the uploaded 1st version -- I want to see different concepts -- definitely want use white space and keep a blue color similiar if not the same as the one seen in that other version and see my notes/feedback.

:

Target Market(s)

Women + Men - 35-60
Self Help + Health

Industry/Entity Type

Health And Wellness

Font styles to use
Sans Serif

Colors
0692cd
34a7d7
85cae6
cee9f5

Requirements
Must have
• Picture of father and I that can be found here:(https://files.cloudvault-share.net/folders/7K9QxRm2_41PlVnwTbZuLeHsCq3)
• and I uploaded one too (I'd like to see it with our shirts on and off)
Nice to have
• Want it to be clean
• More gender neutral -- not overly masculine or femine
• I really like these book covers - so something similair woudl be great"
• Steady Steps: The 9-Week Meal Rhythm Method
• The Quiet Harvest Plan : Retune Your Habits for Gentle Fat Burning, Steady Vigor and Lasting Stamina
• Walk Far, Feel Light for Years

```html
<!DOCTYPE html>
<html lang="en">
<head>
<meta charset="utf-8">
<title>Summit Drive — Book Cover</title>
<link rel="stylesheet" href="https://fonts.googleapis.com/css2?family=Oswald:wght@500&family=Fira+Sans+Condensed:ital,wght@0,500;1,400&family=Lato:wght@400&display=swap">
<style>
  :root {
    --paper: #ffffff;
    --blue: #2f86e2;
    --blue-deep: #1f73d6;
    --blue-light: #5aa6ee;
    --ink-white: #ffffff;
    --photo-light: #f1ece6;
    --photo-skin: #d9a07c;
    --photo-shorts: #5a8fc4;
  }
  * { margin: 0; padding: 0; box-sizing: border-box; }
  html, body {
    width: 900px;
    height: 1200px;
    overflow: hidden;
    background: var(--paper);
  }
  .cover {
    position: relative;
    width: 900px;
    height: 1200px;
    background: var(--paper);
    overflow: hidden;
  }
  .cover-title {
    position: absolute;
    left: 22px;
    top: 30px;
    font-family: "Oswald", "Arial Narrow", sans-serif;
    font-weight: 500;
    font-size: 270px;
    line-height: 0.86;
    letter-spacing: -2px;
    color: var(--blue);
    text-transform: uppercase;
  }
  .cover-title span { display: block; }
  .author-photo {
    position: absolute;
    left: 445px;
    top: 410px;
    width: 440px;
    height: 650px;
    background: linear-gradient(180deg, var(--photo-light) 0%, var(--photo-skin) 30%, var(--photo-skin) 55%, var(--photo-shorts) 70%, var(--photo-skin) 85%, var(--photo-light) 100%);
    border-radius: 160px 160px 20px 20px;
    opacity: 0.85;
  }
  .subtitle-band {
    position: absolute;
    left: 0;
    top: 720px;
    width: 540px;
    height: 116px;
    background: linear-gradient(180deg, var(--blue-light), var(--blue));
    padding: 22px 0 0 58px;
    font-family: "Fira Sans Condensed", "Arial Narrow", sans-serif;
    font-weight: 500;
    font-size: 32px;
    line-height: 1.2;
    color: var(--ink-white);
    text-transform: uppercase;
  }
  .author-band {
    position: absolute;
    left: 0;
    top: 1010px;
    width: 900px;
    height: 140px;
    background: linear-gradient(180deg, var(--blue-light), var(--blue-deep));
    padding: 14px 0 0 60px;
    color: var(--ink-white);
  }
  .author-names {
    font-family: "Lato", Arial, sans-serif;
    font-weight: 400;
    font-size: 72px;
    line-height: 1;
    text-transform: uppercase;
    letter-spacing: 1px;
  }
  .author-tagline {
    margin: 6px 0 0 100px;
    font-family: "Fira Sans Condensed", "Arial Narrow", sans-serif;
    font-style: italic;
    font-weight: 400;
    font-size: 40px;
    line-height: 1;
  }
</style>
</head>
<body>
  <main class="cover">
    <h1 class="cover-title"><span>Summit</span><span>Drive</span></h1>
    <div class="author-photo" role="img" aria-label="Photo of the father and son authors standing side by side, arms crossed, in swim shorts"></div>
    <p class="subtitle-band">Push Past Your Limits,<br>Find Strength Within Yourself</p>
    <footer class="author-band">
      <p class="author-names">Dana &amp; Cole Marsh</p>
      <p class="author-tagline">The father and son fitness team</p>
    </footer>
  </main>
</body>
</html>
```